Coastal Rubdown Oil Co. needs a new label.

This massage oil has been in Australia for over 20 years and needs a new label for its plastic 250ml bottles. The current label (8cm x 8cm) looks old fashioned and so we are looking for something that reflects freedom, relaxation, inspiration. The product is made from sweet almond oil and has different essential oils used to give unique smells. I have seen some lovely abstract vector images. I think we need a clean straight look with bright colours. There are currently six variations to the product. "Weary and Worn Heads, Achy and Spent Frames, Couples Mix, Heather Soak Oil, Unwinding Mix, Uplift Mix" Different coloured labels have been used for each of the blends. I have included photos of existing bottles plus some ideas for the labels.

I would like to use the same font on the name of the brand Bramblewick Acres. If we change the font it may be difficult for existing customers to find our product.

Also just under the name Bramblewick Acres I would like to insert a type of logo (can be the shape of a tear drop or round circle) to say:

Massage Oil
Since 1970

The size of the label is 8cm x 12 cm for the front and the same size for the back of the label.
Updates

Coastal Rubdown oil Company has posted on the brief some images from Pixelvault plus two photos of the original bottles. I am looking for a new design which is bright in colour, fun and funky. I am not thinking along the lines of the traditional Herb and trees look. I think the original label is too busy and the colours overpower the label. The other point I think that is important is that the product has been around since 1970. If there is room I think a round logo which says: Massage Oil Since 1970 I am hoping that we can fit this information on the label Looking forward to seeing all the designs come thru. So far I have only had two designs come thru. Speak soon from hot sunny Australia. maree

Thank you to everyone who has already posted designs for our Massage Label. I have now edited the brief to include some more ideas on how to make this design the Best! I will email back to you straight away ideas and thoughts on your designs. Remember I live in Australia and can be either 10hrs in front or behind your time.

Reason: Due to busy lives and commitments over the next few days I feel that an extension will benefit all involved. Thank you to everyone who has submitted designs and working with me to create something beautiful. maree

Hello from Australia all the designers who have submitted some wonderful designs over the past two weeks. We are now entering the final three days of the competition. Thank you to everyone who has worked so hard to try and create the perfect label for my massage oil bottle. All of you have done a fantastic job. This has made the decision hard to make. Thank you to everyone. Please submit all your last minute designs soon. kind regards maree Australia

Target Market(s)

The type of person purchasing a massage oil blend will buy from a health food shop, pharmacy or from an on-line store. I believe they are wanting something bright that clearly communicates that that it is a massage oil.

Industry/Entity Type

Massage

Font styles to use
Script

Requirements
Must have
• Different colour for each massage oil blend.
Need same font for the name Bramblewick Acres. (script font or similar)

Abstract design please.
Nice to have
• A logo under the name Bramblewick Acres

Tear Drop or circle design that says:

Massage Oil
Since 1970

also we would like an outline for the back label. (see photo attached)

BACK LABEL information

A unique blend of essential oils in a fine light base.

Contains:

vegetable oil extract of nettle, sweet almond oil, ethanol, essential oils of lavender, lemongrass, orange & ylang ylang and vitamin E.

How to Use:

Shake well warm bottle in warm water if very cold.
Lovingly massage the body from head to toe.
Not for medicinal use.

Bramblewick Acres
Hollin WA 6099
Phone: (08) 9555 0142

(LEAVE ROOM FOR BARCODE)
Should not have
• Too busy design or old fashioned design.
No dull colours.

```html
<!DOCTYPE html>
<html lang="en">
<head>
<meta charset="utf-8">
<title>Bramblewick Acres – Massage Oil Labels</title>
<link rel="stylesheet" href="https://fonts.googleapis.com/css2?family=Arimo&family=Ubuntu:wght@500;700&family=Kalam&family=Dancing+Script:wght@600&display=swap">
<style>
  :root {
    --yellow: #ffff00;
    --white-soft: rgba(255,255,255,0.88);
    --orange: #f7821e;
    --orange-ink: #e8341c;
    --blue: #2f9fd3;
    --blue-ink: #1f9a3a;
    --purple: #bb4ee8;
    --purple-ink: #b23de0;
    --pink: #f54fa6;
    --pink-ink: #ee3f9a;
    --text-dark: #1d1d1d;
  }
  * { margin: 0; padding: 0; box-sizing: border-box; }
  html, body { width: 1200px; height: 1083px; overflow: hidden; background: #fff; }
  .sheet { position: relative; width: 1200px; height: 1083px; }

  .label {
    position: absolute;
    width: 280px;
    height: 535px;
    border-radius: 12px;
    overflow: hidden;
    background: var(--tone);
  }
  .orange { --tone: var(--orange); --ink: var(--orange-ink); }
  .blue   { --tone: var(--blue);   --ink: var(--blue-ink); }
  .purple { --tone: var(--purple); --ink: var(--purple-ink); }
  .pink   { --tone: var(--pink);   --ink: var(--pink-ink); }

  .pattern { position: absolute; inset: 0; background: linear-gradient(160deg, rgba(255,255,255,0.06), rgba(0,0,0,0.05)); }

  /* yellow band shared by both faces */
  .band { position: absolute; left: 0; right: 0; top: 425px; height: 75px; background: var(--yellow); }
  .band::after { content: ""; position: absolute; left: 0; right: 0; top: 7px; height: 6px; background: var(--tone); }

  /* back face */
  .intro {
    position: absolute; left: 22px; top: 28px; width: 236px; height: 82px;
    border-radius: 18px; background: var(--white-soft);
    font-family: "Kalam", cursive; font-size: 13px; line-height: 21px;
    text-align: center; color: var(--text-dark); padding-top: 20px;
  }
  .details {
    position: absolute; left: 22px; top: 120px; width: 236px; height: 310px;
    border-radius: 14px 14px 0 0; background: var(--white-soft);
    font-family: "Arimo", sans-serif; font-size: 11.2px; line-height: 13.6px;
    text-align: center; color: var(--text-dark); padding: 14px 10px 0;
  }
  .details h3 { font-weight: 400; font-size: 12.5px; margin-bottom: 14px; }
  .details p { margin-bottom: 13px; }
  .barcode-space { position: absolute; left: 60px; top: 431px; width: 161px; height: 99px; background: #fff; }

  /* front face */
  .brand {
    position: absolute; left: 0; right: 0; top: 50px;
    display: flex; align-items: center; justify-content: center; gap: 10px;
    font-family: "Ubuntu", sans-serif; font-weight: 700; font-size: 30px; line-height: 32px;
    color: #fff; text-align: center;
  }
  .brand .dot { width: 14px; height: 14px; border-radius: 50%; background: #fff; flex: none; }
  .seal {
    position: absolute; left: 51px; top: 193px; width: 178px; height: 232px;
    background: linear-gradient(180deg, rgba(255,255,255,0.75), rgba(255,255,255,0.25));
    border-radius: 50% 50% 0 0 / 14px 14px 0 0;
  }
  .seal-title {
    position: absolute; left: 0; right: 0; top: 250px;
    font-family: "Ubuntu", sans-serif; font-weight: 500; font-size: 20px; line-height: 23px;
    text-align: center; color: var(--text-dark);
  }
  .blend {
    position: absolute; left: 0; right: 0; top: 390px;
    font-family: "Arimo", sans-serif; font-size: 18px; text-align: center; color: #fff;
  }
  .tagline {
    position: absolute; left: 0; right: 0; top: 455px;
    font-family: "Dancing Script", cursive; font-weight: 600; font-size: 21px;
    text-align: center; color: var(--ink);
  }
  .volume {
    position: absolute; left: 0; right: 0; top: 497px;
    font-family: "Arimo", sans-serif; font-size: 17px; text-align: center; color: #fff;
  }
</style>
</head>
<body>
<div class="sheet">

  <!-- Orange pair -->
  <section class="label back orange" style="left:0;top:0">
    <div class="pattern" role="img" aria-label="Faint leaf and butterfly pattern"></div>
    <div class="band"></div>
    <div class="intro">A unique blend of essential oils<br>in a fine light base.</div>
    <div class="details">
      <h3>Contains:</h3>
      <p>vegetable oil extract of nettle, sweet almond oil, ethanol, essential oils of lavender, lemongrass, orange &amp; ylang ylang and vitamin E.</p>
      <h3>How to Use:</h3>
      <p>Shake well warm bottle in warm water if very cold.<br>Lovingly massage the body from head to toe.<br>Not for medicinal use.</p>
      <p>Bramblewick Acres<br>Hollin WA 6099<br>Phone: (08) 9555 0142</p>
    </div>
    <div class="barcode-space"></div>
  </section>
  <section class="label front orange" style="left:302px;top:0">
    <div class="pattern" role="img" aria-label="Faint leaf and butterfly pattern"></div>
    <div class="brand"><span class="dot"></span><span>Bramblewick<br>Acres</span></div>
    <div class="seal"></div>
    <div class="seal-title">Massage Oil<br>Since 1970</div>
    <div class="blend">For Weary &amp; Worn Heads</div>
    <div class="band"></div>
    <div class="tagline">Twenty year of natural skin care</div>
    <div class="volume">250ml</div>
  </section>

  <!-- Blue pair -->
  <section class="label back blue" style="left:619px;top:0">
    <div class="pattern" role="img" aria-label="Faint leaf and butterfly pattern"></div>
    <div class="band"></div>
    <div class="intro">A unique blend of essential oils<br>in a fine light base.</div>
    <div class="details">
      <h3>Contains:</h3>
      <p>vegetable oil extract of nettle, sweet almond oil, ethanol, essential oils of lavender, lemongrass, orange &amp; ylang ylang and vitamin E.</p>
      <h3>How to Use:</h3>
      <p>Shake well warm bottle in warm water if very cold.<br>Lovingly massage the body from head to toe.<br>Not for medicinal use.</p>
      <p>Bramblewick Acres<br>Hollin WA 6099<br>Phone: (08) 9555 0142</p>
    </div>
    <div class="barcode-space"></div>
  </section>
  <section class="label front blue" style="left:920px;top:0">
    <div class="pattern" role="img" aria-label="Faint leaf and butterfly pattern"></div>
    <div class="brand"><span class="dot"></span><span>Bramblewick<br>Acres</span></div>
    <div class="seal"></div>
    <div class="seal-title">Massage Oil<br>Since 1970</div>
    <div class="blend">Unwinding Mix</div>
    <div class="band"></div>
    <div class="tagline">Twenty year of natural skin care</div>
    <div class="volume">250ml</div>
  </section>

  <!-- Purple pair -->
  <section class="label back purple" style="left:0;top:548px">
    <div class="pattern" role="img" aria-label="Faint leaf and butterfly pattern"></div>
    <div class="band"></div>
    <div class="intro">A unique blend of essential oils<br>in a fine light base.</div>
    <div class="details">
      <h3>Contains:</h3>
      <p>vegetable oil extract of nettle, sweet almond oil, ethanol, essential oils of lavender, lemongrass, orange &amp; ylang ylang and vitamin E.</p>
      <h3>How to Use:</h3>
      <p>Shake well warm bottle in warm water if very cold.<br>Lovingly massage the body from head to toe.<br>Not for medicinal use.</p>
      <p>Bramblewick Acres<br>Hollin WA 6099<br>Phone: (08) 9555 0142</p>
    </div>
    <div class="barcode-space"></div>
  </section>
  <section class="label front purple" style="left:302px;top:548px">
    <div class="pattern" role="img" aria-label="Faint leaf and butterfly pattern"></div>
    <div class="brand"><span class="dot"></span><span>Bramblewick<br>Acres</span></div>
    <div class="seal"></div>
    <div class="seal-title">Massage Oil<br>Since 1970</div>
    <div class="blend">Heather Soak Oil</div>
    <div class="band"></div>
    <div class="tagline">Twenty year of natural skin care</div>
    <div class="volume">250ml</div>
  </section>

  <!-- Pink pair -->
  <section class="label back pink" style="left:619px;top:548px">
    <div class="pattern" role="img" aria-label="Faint leaf and butterfly pattern"></div>
    <div class="band"></div>
    <div class="intro">A unique blend of essential oils<br>in a fine light base.</div>
    <div class="details">
      <h3>Contains:</h3>
      <p>vegetable oil extract of nettle, sweet almond oil, ethanol, essential oils of lavender, lemongrass, orange &amp; ylang ylang and vitamin E.</p>
      <h3>How to Use:</h3>
      <p>Shake well warm bottle in warm water if very cold.<br>Lovingly massage the body from head to toe.<br>Not for medicinal use.</p>
      <p>Bramblewick Acres<br>Hollin WA 6099<br>Phone: (08) 9555 0142</p>
    </div>
    <div class="barcode-space"></div>
  </section>
  <section class="label front pink" style="left:920px;top:548px">
    <div class="pattern" role="img" aria-label="Faint leaf and butterfly pattern"></div>
    <div class="brand"><span class="dot"></span><span>Bramblewick<br>Acres</span></div>
    <div class="seal"></div>
    <div class="seal-title">Massage Oil<br>Since 1970</div>
    <div class="blend">Couples Mix</div>
    <div class="band"></div>
    <div class="tagline">Twenty year of natural skin care</div>
    <div class="volume">250ml</div>
  </section>

</div>
</body>
</html>
```